Design an Exhibition Poster for our Web Application

Our company develops and sells VaultLarkly, a web-based service that helps small businesses to test their web applications for security vulnerabilities.

You can see details of the service at the following page:

https://www.vaultlarkly.example/

We need a poster designed, to be used on an exhibition stand at a professional security conference.

Reason: The deadline for this project is being extended because we have, so far, received very few design submissions and they are generally not of the aesthetic quality we are looking for.

Target Market(s)

Tech startups and small / medium sized online businesses

Industry/Entity Type

Security

Requirements
Must have
• [1] Incorporate the VaultLarkly logo (see attached file).

[2] Use the text supplied by us (see attached file).

[3] Use a color scheme that matches the scheme used on our website.

[4] Project the visual theme of cyber security (or protection against cyber crime).
Nice to have
• This is part of a 2-poster set. The project for designing the other poster in the set is also being listed on ArtHivePlace today. Please look for the project entitled "Design an Exhibition Poster for our Software Product".

Preference will be given to designers who submit a pair of designs that harmonize with each other.

```html
<!DOCTYPE html>
<html lang="en">
<head>
<meta charset="utf-8">
<title>VaultLarkly – Security For Web Startups</title>
<link rel="stylesheet" href="https://fonts.googleapis.com/css2?family=Baloo+2:wght@600&family=Quicksand:wght@600;700&family=Fredoka:wght@600&family=Yanone+Kaffeesatz:wght@700&display=swap">
<style>
  :root {
    --green-deep: #3f7a0c;
    --green-mid: #6aa81a;
    --green-bright: #a6e22e;
    --charcoal: #3a3a3a;
    --panel: rgba(38, 38, 36, 0.9);
    --white: #ffffff;
    --logo-grey: #a9a9a9;
    --logo-green: #8cc63f;
  }
  html, body {
    margin: 0;
    padding: 0;
    overflow: hidden;
    background: #ffffff;
  }
  .poster {
    position: relative;
    width: 900px;
    height: 1200px;
    overflow: hidden;
    background:
      radial-gradient(ellipse 55% 30% at 92% 56%, rgba(200,255,90,0.55), transparent 70%),
      radial-gradient(ellipse 70% 55% at 55% 45%, var(--green-mid), transparent 80%),
      linear-gradient(160deg, var(--green-deep) 0%, var(--green-mid) 45%, #4e8c10 100%);
  }
  .tagline-bar {
    position: absolute;
    left: 0;
    top: 18px;
    width: 900px;
    height: 124px;
    background: var(--charcoal);
    color: var(--white);
    font-family: "Baloo 2", sans-serif;
    font-weight: 600;
    font-size: 31px;
    line-height: 40px;
    text-align: center;
    padding-top: 20px;
    box-sizing: border-box;
  }
  .headline {
    position: absolute;
    left: 0;
    top: 198px;
    width: 900px;
    margin: 0;
    text-align: center;
    color: var(--white);
    font-family: "Yanone Kaffeesatz", sans-serif;
    font-weight: 700;
    font-size: 118px;
    line-height: 1;
    transform: skewX(-8deg) rotate(-2deg);
    text-shadow: 0 3px 6px rgba(0,0,0,0.25);
  }
  .panel-shape {
    position: absolute;
    left: 0;
    top: 0;
  }
  .features {
    position: absolute;
    left: 182px;
    top: 420px;
    width: 660px;
    color: var(--white);
    font-family: "Quicksand", sans-serif;
    font-weight: 600;
    font-size: 31px;
    line-height: 41px;
    transform: rotate(-3deg);
    transform-origin: left top;
  }
  .feature { margin: 0 0 14px; }
  .feature-title {
    margin: 0;
    font-weight: 700;
    font-size: 46px;
    line-height: 50px;
    letter-spacing: 1px;
  }
  .feature-text { margin: 0; }
  .brand-strip {
    position: absolute;
    left: 72px;
    top: 636px;
    width: 84px;
    height: 466px;
    background: var(--charcoal);
    transform: rotate(-1.5deg);
  }
  .brand-name {
    position: absolute;
    left: 42px;
    top: 178px;
    transform: translate(-50%, -50%) rotate(-90deg);
    white-space: nowrap;
    color: var(--logo-grey);
    font-family: "Quicksand", sans-serif;
    font-weight: 700;
    font-size: 46px;
    margin: 0;
  }
  .brand-mark {
    position: absolute;
    left: 14px;
    bottom: 28px;
    width: 56px;
    height: 56px;
    background: var(--logo-green);
  }
  .cta-box {
    position: absolute;
    left: 195px;
    top: 1046px;
    width: 705px;
    height: 134px;
    background: var(--charcoal);
    color: var(--white);
    font-family: "Fredoka", sans-serif;
    font-weight: 600;
    font-size: 78px;
    line-height: 134px;
    text-align: center;
    margin: 0;
  }
</style>
</head>
<body>
  <main class="poster">
    <p class="tagline-bar">Online website vulnerability scanning<br>that tells you exactly what needs fixing and how to to fix it.</p>

    <h1 class="headline">Security For Web Startups</h1>

    <svg class="panel-shape" width="900" height="1200" viewBox="0 0 900 1200" aria-hidden="true">
      <polygon points="38,402 800,354 862,932 68,988" fill="var(--panel)"/>
    </svg>

    <section class="features">
      <div class="feature">
        <h2 class="feature-title">ACCESIBLE</h2>
        <p class="feature-text">VaultLarkly runs in the cloud<br>and is accessible from any computer,<br>anywhere, any time.</p>
      </div>
      <div class="feature">
        <h2 class="feature-title">AFFORDBLE</h2>
        <p class="feature-text">VaultLarkly uses a flexible<br>pay-as-you-go model<br>that will fit any budget.</p>
      </div>
      <div class="feature">
        <h2 class="feature-title">SIMPLE</h2>
        <p class="feature-text">Launch your scan using a simple<br>3-step wizard and we'll do the rest.</p>
      </div>
    </section>

    <div class="brand-strip">
      <p class="brand-name">VaultLarkly</p>
      <div class="brand-mark"></div>
    </div>

    <p class="cta-box">Try it Free Today!</p>
  </main>
</body>
</html>
```